New Packaging Design Project

Wine packaging redesign. Retail partner requested a redesign of a private label wine. The old label is attached. Our partner liked the Lantern and Briar label and wanted something similar. There will be a logo added to the top of the label

Went on vacation/holiday

```html
<!DOCTYPE html>
<html lang="en">
<head>
<meta charset="UTF-8">
<title>Napa Valley Red Blend 2018 – Wine Label</title>
<link rel="stylesheet" href="https://fonts.googleapis.com/css2?family=Poiret+One&family=Oswald:wght@300;400&display=swap">
<style>
  :root {
    --sky: #686766;
    --ground: #505050;
    --ridge-dark: #3b3b3b;
    --ridge-slate: #5a5a63;
    --hills: #726d66;
    --river: #ece6df;
    --gold: #e3b050;
    --title-grey: #cac7c7;
    --varietal-grey: #9c9b9b;
    --vintage: #efebe5;
  }
  * { margin: 0; padding: 0; box-sizing: border-box; }
  html, body {
    width: 683px;
    height: 1200px;
    overflow: hidden;
    background: var(--ground);
  }
  .label {
    position: relative;
    width: 683px;
    height: 1200px;
    background: linear-gradient(to bottom, var(--sky) 0, var(--sky) 330px, var(--ground) 330px);
    overflow: hidden;
  }
  .region-title {
    position: absolute;
    top: 118px;
    left: 0;
    width: 683px;
    height: 125px;
  }
  .region-title text {
    font-family: "Poiret One", sans-serif;
    fill: var(--gold);
  }
  .landscape {
    position: absolute;
    top: 330px;
    left: 0;
    width: 683px;
    height: 520px;
    background: linear-gradient(to bottom,
      var(--sky) 0%,
      var(--ridge-dark) 22%,
      var(--ridge-dark) 40%,
      var(--ridge-slate) 55%,
      var(--hills) 68%,
      var(--hills) 80%,
      var(--river) 88%,
      var(--ground) 96%);
  }
  .wine-info {
    position: absolute;
    top: 905px;
    left: 0;
    width: 683px;
    text-align: center;
    font-family: "Oswald", sans-serif;
  }
  .wine-type {
    margin-left: -10px;
    font-weight: 300;
    font-size: 53px;
    line-height: 70px;
    letter-spacing: 4px;
    color: var(--title-grey);
  }
  .varietals {
    margin-top: 12px;
    font-weight: 300;
    font-size: 24px;
    line-height: 32px;
    letter-spacing: 0.3px;
    color: var(--varietal-grey);
    word-spacing: 4px;
  }
  .vintage {
    margin-top: 24px;
    font-weight: 400;
    font-size: 34px;
    line-height: 40px;
    letter-spacing: 2px;
    color: var(--vintage);
  }
</style>
</head>
<body>
  <main class="label">
    <svg class="region-title" viewBox="0 0 683 125" aria-label="Napa Valley">
      <text x="68" y="117" font-size="162" textLength="556" lengthAdjust="spacingAndGlyphs">NAPA VALLEY</text>
    </svg>

    <div class="landscape" role="img" aria-label="Layered mountain ridges above a pale river with vineyard rows in the valley"></div>

    <section class="wine-info">
      <h1 class="wine-type">RED BLEND</h1>
      <p class="varietals">MERLOT&nbsp;|&nbsp; CABERNET SAUVIGNON<br>CABERNET FRANC&nbsp;|&nbsp; PETIT VERDOT&nbsp;|&nbsp; MALBEC</p>
      <p class="vintage">2018</p>
    </section>
  </main>
</body>
</html>
```